Quiet Harbor Candle Company needs a Label design

We need a label design for a new candle company based in Charleston South Carolina. Our mission is to provide people with candles that will fill any space with fragrances that are uplifting, comforting, fresh and will make any space feel like home. Our candles are aromatherapy, 100% soy wax, and hand poured (we would love for this to be indicated somewhere on the label). We would like to see a label that is modern, very clean and uses pastel colors like green, blush pink, mauve and blush blue. The final design should communicate peace, gratitude, hope, and happiness.

```html
<!DOCTYPE html>
<html lang="en">
<head>
<meta charset="UTF-8">
<title>Quiet Harbor Candle Company – Labels</title>
<link href="https://fonts.googleapis.com/css2?family=Jost:wght@400;500&display=swap" rel="stylesheet">
<style>
  :root {
    --canvas: #f8f8f1;
    --label: #ffffff;
    --ink-dark: #2f3d39;
    --sage: #9cb3ac;
    --lavender: #a39fb9;
    --shadow: rgba(60, 70, 65, 0.08);
  }
  * { margin: 0; padding: 0; box-sizing: border-box; }
  html, body {
    width: 1200px;
    height: 900px;
    overflow: hidden;
    background: var(--canvas);
  }
  .canvas {
    width: 1200px;
    height: 900px;
    display: flex;
    align-items: center;
    justify-content: center;
    gap: 70px;
    font-family: "Jost", sans-serif;
  }
  .label {
    width: 440px;
    height: 380px;
    background: var(--label);
    border-radius: 34px;
    box-shadow: 0 6px 24px var(--shadow);
    display: flex;
    flex-direction: column;
    align-items: center;
    padding-top: 46px;
  }
  .brand {
    display: flex;
    flex-direction: column;
    align-items: center;
    gap: 14px;
    height: 150px;
  }
  .brand-dot {
    width: 40px;
    height: 40px;
    border-radius: 50%;
    background: var(--ink-dark);
  }
  .brand-name {
    color: var(--ink-dark);
    font-weight: 400;
    font-size: 22px;
    letter-spacing: 0.06em;
    text-align: center;
    line-height: 1.3;
  }
  .brand-name span {
    display: block;
    font-size: 11px;
    letter-spacing: 0.5em;
    margin-top: 8px;
  }
  .scent {
    font-size: 38px;
    font-weight: 400;
    margin-top: 36px;
    letter-spacing: 0.01em;
  }
  .details {
    margin-top: 14px;
    text-align: center;
    font-size: 16px;
    letter-spacing: 0.05em;
    line-height: 1.45;
    text-transform: uppercase;
  }
  .label--eucalyptus .scent,
  .label--eucalyptus .details { color: var(--sage); }
  .label--lavender .scent,
  .label--lavender .details { color: var(--lavender); }
</style>
</head>
<body>
  <main class="canvas">
    <section class="label label--eucalyptus">
      <div class="brand">
        <div class="brand-dot"></div>
        <div class="brand-name">Quiet Harbor<span>Candle Company</span></div>
      </div>
      <h2 class="scent">Eucalyptus Mint</h2>
      <p class="details">All Natural Aromatherapy<br>Hand Poured | 100% Soy Wax</p>
    </section>

    <section class="label label--lavender">
      <div class="brand">
        <div class="brand-dot"></div>
        <div class="brand-name">Quiet Harbor<span>Candle Company</span></div>
      </div>
      <h2 class="scent">Lavender Vanilla</h2>
      <p class="details">All Natural Aromatherapy<br>Hand Poured | 100% Soy Wax</p>
    </section>
  </main>
</body>
</html>
```